Tova Brisk Fitness Coaching Project

I am a personal trainer based in London. My services include one-on-one PT sessions, bootcamps.
I would like the design to be minimalistic. With light colours: white, pink, purple.
I specialise in weight loss, flexibility, mobility.

Tova Penrick
Personal Trainer
Email: tova.penrick@mailgrove.net
tel: 07500 918 243
picturely: Tova Brisk

Target Market(s)

adults, mostly females (age 18-50).

Industry/Entity Type

Fitness

Contact Information for Business Card

Tova Penrick
Personal Trainer
tel: 07500 918 243
picturely: Tova Brisk

Font styles to use
Serif

Colors
eea4c8
fbd4d5
fdf9cf
cfeae6
cee9f5

Requirements
Nice to have
• minimalistic style
• easy to read and remember

```html
<!DOCTYPE html>
<html lang="en">
<head>
<meta charset="utf-8">
<title>Tova Brisk Fitness Coaching – Business Card</title>
<link rel="stylesheet" href="https://fonts.googleapis.com/css2?family=Libre+Baskerville:wght@400;700&display=swap">
<style>
  :root {
    --backdrop: #e6e2dd;
    --card: #ffffff;
    --pink: #eea4c8;
    --ink: #1f1f1f;
    --photo-pink: #e4167e;
    --photo-teal: #3cc3cc;
    --photo-dark: #1f3b44;
  }
  * { box-sizing: border-box; margin: 0; padding: 0; }
  html, body { width: 1200px; height: 1000px; overflow: hidden; }
  body {
    background: var(--backdrop);
    font-family: "Libre Baskerville", Georgia, serif;
    color: var(--ink);
    position: relative;
  }
  .card {
    position: absolute;
    top: 340px;
    width: 540px;
    height: 320px;
    background: var(--card);
    border-radius: 26px;
    overflow: hidden;
    box-shadow: 0 6px 18px rgba(0,0,0,0.12);
  }
  .card-back { left: 40px; }
  .card-front { left: 620px; }
  .accent-band {
    position: absolute;
    left: 0; right: 0; bottom: 0;
    height: 18px;
    background: var(--pink);
  }

  /* back side */
  .action-photo {
    position: absolute;
    left: 0; top: 0; right: 0;
    height: 200px;
    background:
      linear-gradient(180deg, var(--photo-pink) 0%, var(--photo-pink) 28%, var(--photo-teal) 32%, var(--photo-teal) 78%, var(--photo-dark) 100%);
  }
  .social-handle {
    position: absolute;
    left: 0; right: 0; top: 236px;
    display: flex;
    justify-content: center;
    align-items: center;
    gap: 12px;
    font-size: 17px;
    letter-spacing: 0.3px;
  }
  .social-mark {
    width: 18px; height: 18px;
    border: 2px solid var(--pink);
    border-radius: 4px;
  }

  /* front side */
  .portrait {
    position: absolute;
    left: 209px; top: 34px;
    width: 110px; height: 110px;
    border-radius: 50%;
    background: radial-gradient(circle at 50% 45%, #b07a5c 0%, #5a3322 60%, #3b5a2e 100%);
  }
  .identity {
    position: absolute;
    left: 16px; width: 236px; top: 176px;
    text-align: center;
  }
  .identity .name {
    color: var(--pink);
    font-size: 28px;
    font-weight: 700;
    letter-spacing: 0.3px;
    white-space: nowrap;
  }
  .identity .role {
    margin-top: 8px;
    font-size: 15px;
  }
  .divider {
    position: absolute;
    left: 264px; top: 150px;
    width: 2px; height: 96px;
    background: var(--pink);
  }
  .contacts {
    position: absolute;
    left: 282px; top: 150px;
    list-style: none;
  }
  .contacts li {
    display: flex;
    align-items: center;
    gap: 8px;
    font-size: 13px;
    height: 34px;
    white-space: nowrap;
  }
  .contacts .phone { font-size: 16px; letter-spacing: 1px; }
  .contacts svg { flex: none; }
</style>
</head>
<body>

  <section class="card card-back" aria-label="Business card back">
    <div class="action-photo" role="img" aria-label="Photo of the trainer stretching in front of a pink and teal painted wall"></div>
    <p class="social-handle"><span class="social-mark"></span>picturely/Tova Brisk</p>
    <div class="accent-band"></div>
  </section>

  <section class="card card-front" aria-label="Business card front">
    <div class="portrait" role="img" aria-label="Portrait photo of Tova Penrick"></div>
    <div class="identity">
      <h1 class="name">Tova Penrick</h1>
      <p class="role">Personal Trainer</p>
    </div>
    <div class="divider"></div>
    <ul class="contacts">
      <li class="phone">
        <svg width="16" height="16" viewBox="0 0 24 24" aria-hidden="true">
          <path fill="#eea4c8" d="M6.6 10.8a15.1 15.1 0 0 0 6.6 6.6l2.2-2.2a1 1 0 0 1 1-.25 11.4 11.4 0 0 0 3.6.57 1 1 0 0 1 1 1V20a1 1 0 0 1-1 1A17 17 0 0 1 3 4a1 1 0 0 1 1-1h3.5a1 1 0 0 1 1 1c0 1.25.2 2.45.57 3.57a1 1 0 0 1-.25 1z"/>
        </svg>
        07500 918 243
      </li>
      <li class="email">
        <svg width="18" height="13" viewBox="0 0 20 14" aria-hidden="true">
          <rect x="1" y="1" width="18" height="12" fill="none" stroke="#eea4c8" stroke-width="1.6"/>
          <path d="M1 1l9 7 9-7" fill="none" stroke="#eea4c8" stroke-width="1.6"/>
        </svg>
        tova.penrick@mailgrove.net
      </li>
    </ul>
    <div class="accent-band"></div>
  </section>

</body>
</html>
```